" SOMOS UMA EMPRESA RECÉM CRIADA (FEVEREIRO DE 2015) E ESTAMOS ESTABELECIDOS NA CIDADE DE SAO JOSÉ DOS CAMPOS. TRATA-SE DE UM ESCRITORIO DE ADVOCACIA QUE É ESPECIALIZADO NA AREA DO DIREITO TRABALHISTA PATRONAL (ADVOGAMOS APENAS PARA EMPRESAS) E DIREITO ADMINISTRATIVO. "

```html
<!DOCTYPE html>
<html lang="pt-BR">
<head>
<meta charset="utf-8">
<title>Papel Timbrado — Prado Vilela &amp; Sena Costa</title>
<link rel="stylesheet" href="https://fonts.googleapis.com/css2?family=Cormorant+Garamond:wght@700&family=Arimo:wght@400;700&display=swap">
<style>
  :root {
    --backdrop: #e4e5e7;
    --paper: #ffffff;
    --navy: #1f2a44;
    --steel: #8a929c;
    --accent: #2b8ccc;
    --text: #3a4150;
  }
  * { box-sizing: border-box; margin: 0; padding: 0; }
  html, body { width: 1200px; height: 1200px; overflow: hidden; }
  body {
    background: var(--backdrop);
    display: flex;
    align-items: center;
    justify-content: center;
    font-family: "Arimo", Arial, sans-serif;
  }
  .letterhead {
    position: relative;
    width: 751px;
    height: 1100px;
    background: var(--paper);
    box-shadow: 0 2px 8px rgba(0,0,0,0.12);
    overflow: hidden;
  }
  .brand {
    position: absolute;
    left: 66px;
    top: 70px;
    display: flex;
    align-items: center;
    gap: 14px;
  }
  .brand-mark {
    width: 46px;
    height: 46px;
    border-radius: 50%;
    background: var(--navy);
  }
  .brand-text { display: flex; flex-direction: column; }
  .brand-name {
    font-family: "Cormorant Garamond", Georgia, serif;
    font-weight: 700;
    font-size: 19px;
    letter-spacing: 0.6px;
    text-transform: uppercase;
    color: var(--navy);
  }
  .brand-tagline {
    margin-top: 3px;
    font-family: "Cormorant Garamond", Georgia, serif;
    font-weight: 700;
    font-size: 9px;
    letter-spacing: 1.4px;
    text-transform: uppercase;
    color: var(--navy);
    align-self: flex-end;
  }
  .contact-bar {
    position: absolute;
    left: 66px;
    right: 40px;
    top: 1022px;
    display: flex;
  }
  .contact {
    display: flex;
    align-items: flex-start;
    gap: 10px;
    font-size: 11px;
    line-height: 15px;
    font-weight: 700;
    color: var(--text);
  }
  .contact-address { width: 255px; }
  .contact-phone { width: 165px; }
  .contact-icon { flex: 0 0 20px; width: 20px; height: 20px; }
  .footer-rule {
    position: absolute;
    left: 0; right: 0;
    bottom: 26px;
    height: 4px;
    background: var(--accent);
  }
  .footer-band {
    position: absolute;
    left: 0; right: 0; bottom: 0;
    height: 24px;
    background: var(--navy);
  }
</style>
</head>
<body>
  <main class="letterhead">
    <header class="brand">
      <span class="brand-mark"></span>
      <div class="brand-text">
        <span class="brand-name">Prado Vilela &amp; Sena Costa</span>
        <span class="brand-tagline">Sociedade de Advogados</span>
      </div>
    </header>

    <footer class="contact-bar">
      <div class="contact contact-address">
        <svg class="contact-icon" viewBox="0 0 20 20" aria-hidden="true">
          <circle cx="10" cy="10" r="10" fill="#2b8ccc"/>
          <path d="M10 4.5a3.6 3.6 0 0 0-3.6 3.6c0 2.7 3.6 6.9 3.6 6.9s3.6-4.2 3.6-6.9A3.6 3.6 0 0 0 10 4.5z" fill="#fff"/>
          <circle cx="10" cy="8.1" r="1.4" fill="#2b8ccc"/>
        </svg>
        <p>Rua das Acácias, 48 / 310 - Centro<br>São José dos Campos - SP - CEP: 12210-00</p>
      </div>
      <div class="contact contact-phone">
        <svg class="contact-icon" viewBox="0 0 20 20" aria-hidden="true">
          <circle cx="10" cy="10" r="10" fill="#2b8ccc"/>
          <path d="M7.2 5.2l1.6 1.6-1 1.4c.7 1.5 1.8 2.6 3.3 3.3l1.4-1 1.6 1.6-1 1.6c-3.6-.3-6.4-3.1-6.7-6.7z" fill="#fff"/>
        </svg>
        <p>(12) 3456-7810<br>(12) 3456-7825</p>
      </div>
      <div class="contact contact-web">
        <svg class="contact-icon" viewBox="0 0 20 20" aria-hidden="true">
          <circle cx="10" cy="10" r="10" fill="#2b8ccc"/>
          <rect x="5" y="6.5" width="10" height="7" rx="1" fill="#fff"/>
          <path d="M5.3 7l4.7 3.6L14.7 7" fill="none" stroke="#2b8ccc" stroke-width="1"/>
        </svg>
        <p>contato@pvsc.adv.br<br>www.pvsc.adv.br</p>
      </div>
    </footer>

    <div class="footer-rule"></div>
    <div class="footer-band"></div>
  </main>
</body>
</html>
```